Menu Design Project

We are a cafe in italy our name is "Bright Corvella Cafe & Food"

We need a new menu we offer cafes and snacks.

our web site is brightcorvella.com you can find there our logo.

We need something clean to print so we can offer to our clients a good menu.

Target Market(s)

cafe clients

Industry/Entity Type

Cafe

Requirements
Must have
• - Nice design
- Our logo
- Demo text so we can write our text

```html
<!DOCTYPE html>
<html lang="en">
<head>
<meta charset="utf-8">
<title>Bright Corvella Cafe &amp; Food — Menu</title>
<link href="https://fonts.googleapis.com/css2?family=Great+Vibes&family=Questrial&family=Open+Sans:wght@400&display=swap" rel="stylesheet">
<style>
  :root {
    --ink: #0b0b0b;
    --orange: #f7941d;
    --paper: #ffffff;
    --text: #111111;
    --muted: #7a7a7a;
    --photo-dark: #0d0f1a;
    --photo-mid: #2a3a3c;
  }
  * { margin: 0; padding: 0; box-sizing: border-box; }
  html, body { width: 849px; height: 1200px; overflow: hidden; background: var(--paper); }
  .menu { position: relative; width: 849px; height: 1200px; overflow: hidden; background: var(--paper); }
  .backdrop { position: absolute; inset: 0; width: 849px; height: 1200px; }
  .brand {
    position: absolute; left: 130px; top: 28px; width: 170px; height: 170px;
    border: 6px solid var(--orange); border-radius: 50%;
    display: flex; align-items: center; justify-content: center; text-align: center;
  }
  .brand-name {
    font-family: "Questrial", sans-serif; font-size: 27px; line-height: 1.15;
    color: var(--orange); font-weight: 400;
  }
  .tagline {
    position: absolute; left: 56px; top: 262px; width: 350px;
    font-family: "Great Vibes", cursive; font-size: 50px; color: var(--paper);
    white-space: nowrap; word-spacing: 6px;
  }
  .dish-photo {
    position: absolute; left: 125px; width: 208px; height: 137px;
    background: radial-gradient(ellipse at 50% 60%, var(--photo-mid) 0%, var(--photo-dark) 70%);
  }
  .dish-entry { position: absolute; left: 430px; width: 330px; height: 90px; text-align: center; }
  .dish-title {
    font-family: "Questrial", sans-serif; font-size: 28px; line-height: 36px;
    font-weight: 400; color: var(--text); white-space: nowrap;
  }
  .dish-price { color: var(--orange); }
  .dish-desc {
    font-family: "Open Sans", sans-serif; font-size: 19px; line-height: 27px; color: var(--muted);
  }
</style>
</head>
<body>
<main class="menu">
  <svg class="backdrop" viewBox="0 0 600 848" preserveAspectRatio="none" aria-hidden="true">
    <path fill="var(--orange)" d="M0 0 H386 C381 100 322 200 287 300 C252 400 322 480 242 530 C182 566 130 582 160 622 C200 682 240 762 246 848 H0 Z"/>
    <path fill="var(--ink)" d="M0 0 H375 C360 110 300 210 270 300 C240 390 242 440 212 470 C162 512 102 542 72 600 C60 680 90 770 90 848 H0 Z"/>
  </svg>

  <div class="brand"><span class="brand-name">Bright<br>Corvella</span></div>
  <div class="tagline">Cafe And Snacks</div>

  <div class="dish-photo" style="top:361px" role="img" aria-label="Photo of a plated gourmet appetizer on a glass dish"></div>
  <div class="dish-photo" style="top:525px" role="img" aria-label="Photo of a plated gourmet appetizer on a glass dish"></div>
  <div class="dish-photo" style="top:695px" role="img" aria-label="Photo of a plated gourmet appetizer on a glass dish"></div>
  <div class="dish-photo" style="top:859px" role="img" aria-label="Photo of a plated gourmet appetizer on a glass dish"></div>
  <div class="dish-photo" style="top:1023px" role="img" aria-label="Photo of a plated gourmet appetizer on a glass dish"></div>

  <section class="dish-entry" style="top:374px">
    <h2 class="dish-title">Food Item <span class="dish-price">- $50.00</span></h2>
    <p class="dish-desc">Food and menu item description here</p>
  </section>
  <section class="dish-entry" style="top:528px">
    <h2 class="dish-title">Food Item <span class="dish-price">- $50.00</span></h2>
    <p class="dish-desc">Food and menu item description here</p>
  </section>
  <section class="dish-entry" style="top:710px">
    <h2 class="dish-title">Food Item <span class="dish-price">- $50.00</span></h2>
    <p class="dish-desc">Food and menu item description here</p>
  </section>
  <section class="dish-entry" style="top:874px">
    <h2 class="dish-title">Food Item <span class="dish-price">- $50.00</span></h2>
    <p class="dish-desc">Food and menu item description here</p>
  </section>
  <section class="dish-entry" style="top:1038px">
    <h2 class="dish-title">Food Item <span class="dish-price">- $50.00</span></h2>
    <p class="dish-desc">Food and menu item description here</p>
  </section>
</main>
</body>
</html>
```